I am a new company with the latest technology in the concrete polishing business

We need a logo design for a new company out of Toronto, Canada. We polish residential, commercial and industrial concrete as well as different epoxy toppings.

Target Market(s)

How Owners with expendable incomes

Industry/Entity Type

Construction

Contact Information for Business Card

be able to see content rather easily

Colors
0355a3
fbed22
1b1b1b

Requirements
Must have
• simple and elegant

```html
<!DOCTYPE html>
<html lang="en">
<head>
<meta charset="utf-8">
<title>Slabline Coatings – Business Card</title>
<link href="https://fonts.googleapis.com/css2?family=Exo+2:wght@500;600;800&display=swap" rel="stylesheet">
<style>
  :root {
    --blue: #0355a3;
    --blue-bright: #2f4fb0;
    --yellow: #fbed22;
    --ink: #1b1b1b;
    --black: #0c0c0c;
    --concrete-light: #4a4a4a;
    --concrete-dark: #2a2a2a;
    --white: #ffffff;
    --backdrop: #dcd8d1;
  }
  * { box-sizing: border-box; margin: 0; padding: 0; }
  html, body {
    width: 900px; height: 1200px; overflow: hidden;
    background: var(--backdrop);
    font-family: "Exo 2", sans-serif;
  }
  .canvas { position: relative; width: 900px; height: 1200px; }

  .card {
    position: absolute; left: 88px; width: 734px; height: 428px;
    border-radius: 22px; overflow: hidden;
    box-shadow: 0 6px 18px rgba(0,0,0,.35);
  }
  .card--front { top: 137px; }
  .card--back { top: 633px; }

  .concrete-surface {
    position: absolute; inset: 0;
    background: radial-gradient(ellipse at 60% 20%, var(--concrete-light) 0%, var(--concrete-dark) 75%);
  }

  /* Front */
  .header-band {
    position: absolute; left: 0; top: 0; width: 100%; height: 155px;
    background: var(--black);
  }
  .header-rule {
    position: absolute; left: 0; top: 155px; width: 100%; height: 9px;
    background: var(--yellow);
  }
  .company-name {
    position: absolute; left: 42px; top: 26px;
    color: var(--white); font-weight: 800; font-size: 50px;
    line-height: 50px; letter-spacing: 1px; text-transform: uppercase;
  }
  .brand-circle {
    position: absolute; left: 377px; top: 100px;
    width: 336px; height: 336px; border-radius: 50%;
    background: var(--blue-bright);
    border: 12px solid var(--yellow);
  }
  .brand-circle--front { left: 377px; top: 30px; width: 336px; height: 336px; }

  .person-name {
    position: absolute; left: 42px; top: 180px;
    color: var(--white); font-weight: 600; font-size: 23px; letter-spacing: 1.5px;
  }
  .person-title {
    position: absolute; left: 42px; top: 212px;
    color: var(--yellow); font-weight: 500; font-size: 17px; letter-spacing: 1.5px;
  }
  .contact-list { position: absolute; left: 42px; top: 252px; list-style: none; }
  .contact-item {
    display: flex; align-items: flex-start; gap: 12px;
    color: var(--white); font-size: 21px; font-weight: 500; line-height: 27px;
    margin-bottom: 5px;
  }
  .contact-item--address { margin-top: 15px; }
  .contact-icon {
    flex: none; width: 26px; height: 26px; border-radius: 4px;
    background: var(--yellow); display: flex; align-items: center; justify-content: center;
  }
  .contact-item--address .contact-icon { height: 44px; margin-top: 4px; }

  .footer-rule {
    position: absolute; left: 0; top: 402px; width: 100%; height: 3px;
    background: var(--white);
  }
  .footer-band {
    position: absolute; left: 0; top: 405px; width: 100%; height: 23px;
    background: var(--blue-bright);
  }

  /* Back */
  .brand-circle--back {
    left: 102px; top: 124px; width: 178px; height: 178px;
    border-width: 8px;
  }
  .divider {
    position: absolute; left: 310px; top: 162px; width: 2px; height: 100px;
    background: rgba(255,255,255,.8);
  }
  .company-name--back { left: 340px; top: 162px; }
</style>
</head>
<body>
<main class="canvas">

  <section class="card card--front" aria-label="Business card front">
    <div class="concrete-surface" role="img" aria-label="Polished grey concrete floor texture"></div>
    <div class="header-band"></div>
    <div class="header-rule"></div>
    <h1 class="company-name">Slabline<br>Coatings</h1>
    <div class="brand-circle brand-circle--front"></div>

    <p class="person-name">MARCO DELANEY</p>
    <p class="person-title">SENIOR TECHNICAL SUPPORT</p>
    <ul class="contact-list">
      <li class="contact-item">
        <span class="contact-icon">
          <svg width="16" height="16" viewBox="0 0 24 24"><path fill="#1b1b1b" d="M6.6 10.8c1.4 2.8 3.8 5.1 6.6 6.6l2.2-2.2c.3-.3.7-.4 1-.2 1.1.4 2.3.6 3.6.6.6 0 1 .4 1 1V20c0 .6-.4 1-1 1C10.6 21 3 13.4 3 4c0-.6.4-1 1-1h3.5c.6 0 1 .4 1 1 0 1.3.2 2.5.6 3.6.1.3 0 .7-.2 1z"/></svg>
        </span>
        (555) 014-2290
      </li>
      <li class="contact-item">
        <span class="contact-icon">
          <svg width="16" height="14" viewBox="0 0 24 20"><rect x="2" y="3" width="20" height="14" fill="none" stroke="#1b1b1b" stroke-width="2"/><path d="M2 3l10 8 10-8" fill="none" stroke="#1b1b1b" stroke-width="2"/></svg>
        </span>
        hello@slablinemail.com
      </li>
      <li class="contact-item contact-item--address">
        <span class="contact-icon">
          <svg width="14" height="20" viewBox="0 0 24 32"><path fill="#1b1b1b" d="M12 1C6 1 2 5.5 2 11c0 7.5 10 20 10 20s10-12.5 10-20C22 5.5 18 1 12 1zm0 14a4 4 0 110-8 4 4 0 010 8z"/></svg>
        </span>
        <span>2150 Cedar Ridge Rd<br>Alder, ON L4K 1B3</span>
      </li>
    </ul>

    <div class="footer-rule"></div>
    <div class="footer-band"></div>
  </section>

  <section class="card card--back" aria-label="Business card back">
    <div class="concrete-surface" role="img" aria-label="Polished grey concrete floor texture"></div>
    <div class="brand-circle brand-circle--back"></div>
    <div class="divider"></div>
    <h2 class="company-name company-name--back">Slabline<br>Coatings</h2>
  </section>

</main>
</body>
</html>
```